Professional & Modern Technology Business Card

We need a business card for our software/technology firm. Our services include Program/Project Management, Project Controls and Enterprise Analytics. Our clients are usually in the Aviation, Public Works, Transportation and Electric & Water Utility industries. We serve both public and private clients. Would like a very professional, conservative but somewhat modern design. Design, Develop, Deploy is the corporate tagline. We have two offices. The headquarters is in Atlanta, GA and a satellite office In Savannah, GA. Corporate Logo Attached.
Looking to do website and corporate brochure after the successful completion of this project. Would like to begin a working relationship with best designers.
Tagline: Design, Develop, Deploy
Website: www.quambelsystems.example
My Name: Delia Marchetti
My Title: CEO
Email: dmarchetti@quambelsystems.example
Atlanta Address:
87 Corliss Avenue, #2260
Atlanta, GA 30301
Office: 404.555.0178
Fax: 404.555.0143
Mobile: 404.555.0116
Savannah Address:
315 West Harrow Lane Street
Suite 720
Savannah, GA 31401
Office: 912.555.0162
Fax: 404.555.0143
Mobile: 404.555.0116
Please include the email address in your designs: dmarchetti@quambelsystems.example.
I appreciate everyone's design efforts. Just a few notes:
1. Please remove the mobile number from the cards
2. The backs of the cards can be utilized for writing notes. Make sure your design on the back of the card is conducive to clearly adding writing if needed.
3. No black backgrounds please
4. Only use the corporate logo on the front of the card. You can use portions of the logo design, but not the logo in totality.
Thank You
Conservative

```html
<!DOCTYPE html>
<html lang="en">
<head>
<meta charset="utf-8">
<title>Quambel Systems – Business Card</title>
<link href="https://fonts.googleapis.com/css2?family=Cinzel:wght@500&family=Crimson+Pro:wght@400;500&display=swap" rel="stylesheet">
<style>
  :root {
    --canvas: #e9ebea;
    --card-front: #f6f8f7;
    --card-back: #ffffff;
    --green: #a6cf4f;
    --ink: #1c1c1c;
    --ink-soft: #333333;
    --black-block: #1f1f1f;
    --rule: #eef0dc;
    --ghost: #ececec;
  }
  * { box-sizing: border-box; margin: 0; padding: 0; }
  html, body { width: 1200px; height: 1000px; overflow: hidden; }
  body {
    background: var(--canvas);
    font-family: "Crimson Pro", Georgia, serif;
    color: var(--ink);
    position: relative;
  }
  .card {
    position: absolute;
    left: 255px;
    width: 690px;
    height: 400px;
    box-shadow: 0 4px 14px rgba(0,0,0,.18);
    overflow: hidden;
  }
  /* ---------- Front ---------- */
  .card-front { top: 66px; background: var(--card-front); }
  .identity { position: absolute; left: 30px; top: 24px; width: 270px; }
  .identity-name {
    font-family: "Cinzel", "Times New Roman", serif;
    font-weight: 500;
    font-size: 31px;
    letter-spacing: .5px;
    line-height: 1;
    white-space: nowrap;
  }
  .identity-title {
    font-family: "Cinzel", "Times New Roman", serif;
    font-size: 21px;
    text-align: right;
    line-height: 1.2;
  }
  .identity-email {
    display: flex; align-items: center; gap: 10px;
    font-size: 16px; margin-top: 2px; white-space: nowrap;
  }
  .brand {
    position: absolute; left: 445px; top: 48px;
    display: flex; align-items: center; gap: 10px;
  }
  .brand-dot { width: 22px; height: 22px; border-radius: 50%; background: var(--green); flex: none; }
  .brand-name {
    font-size: 27px; font-weight: 500; line-height: 1;
    color: var(--ink); width: 170px;
  }
  .office { position: absolute; top: 168px; }
  .office-hq { left: 38px; width: 270px; }
  .office-sav { left: 418px; width: 240px; }
  .office-heading {
    display: flex; align-items: center; gap: 8px;
    font-size: 22px; font-weight: 500; margin-bottom: 12px;
  }
  .office-sav .office-heading { gap: 16px; margin-left: 4px; }
  .office-heading::before, .office-heading::after {
    content: ""; width: 28px; height: 4px; background: var(--ink);
  }
  .contact-row {
    display: flex; align-items: flex-start; gap: 12px;
    font-size: 14.5px; line-height: 1.45; color: var(--ink-soft);
    margin-bottom: 15px;
  }
  .contact-row.address { min-height: 38px; margin-bottom: 14px; }
  .spaced { letter-spacing: 3px; }
  .icon { width: 16px; height: 16px; flex: none; margin-top: 2px; }
  .divider {
    position: absolute; left: 343px; top: 180px;
    width: 2px; height: 165px; background: var(--green);
  }
  .front-band { position: absolute; left: 0; bottom: 0; }

  /* ---------- Back ---------- */
  .card-back { top: 534px; background: var(--card-back); }
  .back-band { position: absolute; left: 0; width: 100%; background: var(--green); }
  .back-band-top { top: 0; height: 42px; }
  .back-band-bottom { bottom: 0; height: 46px; }
  .note-lines { position: absolute; left: 50px; top: 72px; }
  .ghost-name {
    position: absolute; left: 80px; top: 170px;
    font-family: "Cinzel", "Times New Roman", serif;
    font-size: 52px; letter-spacing: 3px;
    color: var(--ghost); white-space: nowrap;
    transform: rotate(-22deg);
  }
  .back-website {
    position: absolute; right: 22px; bottom: 54px;
    font-size: 16px; color: var(--ink);
  }
</style>
</head>
<body>

<!-- Front of card -->
<section class="card card-front" aria-label="Business card front">
  <div class="identity">
    <div class="identity-name">Delia Marchetti</div>
    <div class="identity-title">CEO</div>
    <div class="identity-email">
      <svg class="icon" viewBox="0 0 16 16" aria-hidden="true">
        <rect x="1" y="3" width="14" height="10" fill="#a6cf4f" stroke="#555" stroke-width="1"/>
        <path d="M1 3 L8 9 L15 3" fill="none" stroke="#555" stroke-width="1"/>
      </svg>
      <span>dmarchetti@quambelsystems.example</span>
    </div>
  </div>

  <div class="brand">
    <span class="brand-dot"></span>
    <span class="brand-name">Quambel Systems, Inc.</span>
  </div>

  <div class="office office-hq">
    <div class="office-heading">Headquarters</div>
    <div class="contact-row address">
      <svg class="icon" viewBox="0 0 16 16" aria-hidden="true"><rect width="16" height="16" rx="2" fill="#a6cf4f"/><path d="M8 3a3 3 0 0 1 3 3c0 2.3-3 6-3 6s-3-3.7-3-6a3 3 0 0 1 3-3z" fill="#fff"/><circle cx="8" cy="6" r="1.1" fill="#a6cf4f"/></svg>
      <div>87 Corliss Avenue, #2260<br><span class="spaced">Atlanta, GA 30301</span></div>
    </div>
    <div class="contact-row">
      <svg class="icon" viewBox="0 0 16 16" aria-hidden="true"><rect width="16" height="16" rx="2" fill="#a6cf4f"/><path d="M5 3.5l2 2-1 1.3c.6 1.3 1.6 2.3 2.9 2.9l1.3-1 2 2-1.2 1.5C7.8 12 4 8.2 3.8 4.7z" fill="#fff"/></svg>
      <span>404.555.0178</span>
    </div>
    <div class="contact-row">
      <svg class="icon" viewBox="0 0 16 16" aria-hidden="true"><rect width="16" height="16" rx="2" fill="#a6cf4f"/><rect x="4" y="7" width="8" height="5" fill="none" stroke="#fff" stroke-width="1.3"/><rect x="5.5" y="4" width="5" height="3" fill="#fff"/></svg>
      <span>404.555.0143</span>
    </div>
  </div>

  <div class="divider"></div>

  <div class="office office-sav">
    <div class="office-heading">Savannah</div>
    <div class="contact-row address">
      <svg class="icon" viewBox="0 0 16 16" aria-hidden="true"><rect width="16" height="16" rx="2" fill="#a6cf4f"/><path d="M8 3a3 3 0 0 1 3 3c0 2.3-3 6-3 6s-3-3.7-3-6a3 3 0 0 1 3-3z" fill="#fff"/><circle cx="8" cy="6" r="1.1" fill="#a6cf4f"/></svg>
      <div>315 West Harrow Lane Street<br>Suite 720 Savannah, GA 31401</div>
    </div>
    <div class="contact-row">
      <svg class="icon" viewBox="0 0 16 16" aria-hidden="true"><rect width="16" height="16" rx="2" fill="#a6cf4f"/><path d="M5 3.5l2 2-1 1.3c.6 1.3 1.6 2.3 2.9 2.9l1.3-1 2 2-1.2 1.5C7.8 12 4 8.2 3.8 4.7z" fill="#fff"/></svg>
      <span>912.555.0162</span>
    </div>
    <div class="contact-row">
      <svg class="icon" viewBox="0 0 16 16" aria-hidden="true"><rect width="16" height="16" rx="2" fill="#a6cf4f"/><rect x="4" y="7" width="8" height="5" fill="none" stroke="#fff" stroke-width="1.3"/><rect x="5.5" y="4" width="5" height="3" fill="#fff"/></svg>
      <span>404.555.0143</span>
    </div>
  </div>

  <svg class="front-band" width="690" height="60" viewBox="0 340 690 60" aria-hidden="true">
    <rect x="0" y="355" width="690" height="45" fill="#a6cf4f"/>
    <polygon points="578,377 588,355 606,355 596,377 606,400 588,400" fill="#ffffff"/>
    <polygon points="596,377 606,355 690,355 690,400 606,400" fill="#1f1f1f"/>
  </svg>
</section>

<!-- Back of card -->
<section class="card card-back" aria-label="Business card back">
  <div class="back-band back-band-top"></div>
  <svg class="note-lines" width="600" height="220" viewBox="0 0 600 220" aria-hidden="true">
    <g stroke="#eef0dc" stroke-width="1.5" stroke-dasharray="8 4">
      <line x1="0" y1="10" x2="600" y2="10"/>
      <line x1="0" y1="46" x2="600" y2="46"/>
      <line x1="0" y1="82" x2="600" y2="82"/>
      <line x1="0" y1="118" x2="600" y2="118"/>
      <line x1="0" y1="154" x2="600" y2="154"/>
      <line x1="0" y1="190" x2="600" y2="190"/>
    </g>
  </svg>
  <div class="ghost-name" aria-hidden="true">Delia Marchetti</div>
  <div class="back-website">www.quambelsystems.example</div>
  <div class="back-band back-band-bottom"></div>
</section>

</body>
</html>
```